Off Grid consulting and outdoor products needs a website

We need a website design to help launch our new business. Its a business that plans to offer Off-grid conslting and outdoor survival products to people who are looking to relocate or vacation to properties/homes that are Off-grid. We plan to offer design plans for homes/cabins, renewable energy systems for power/heating etc, survival products for outdoor vacations/living. We also do consulting and project management for those who want to design and build from scratch their dream off-grid home or vacation property. I've included our logo design for use.
Would like the website to include 5 pages.
www.ridgepinehaven.com
The main landing page (1)
want a video loop backround with a flyover of a cabin in the woods.
https://www.clipvaultora.com/video/clip-48291736-blue-sky-melting-snow-on-green-energy
(also need a backup static image of just high-shot of cabin in woods)
logo top left, Quoted string of text in the middle, over the video. and a CTA button to 'Contact us'
picture links below that to last 3 recent blog posts.
About Us page (2)
(example) https://larkwildgear.com/pages/about-lark
Blog page (3)
blog posts associated with pictures.
Consulting 'services' page (4)
-land services and moving off-grid
-Building off grid
-Renewable energy off-grid
-Sustainable farming and all season greenhouses
Store page 'comming soon' (5)
(Example) http://timberly.crestlayouts.com/demo-1/demo.html

Target Market(s)

Outdoor enthusiasts and people who want to escape their city life

Coding

Coded - Design and coding required

Requirements
Must have
• Outdoor feel, woods, cabin, reneable energy (solar, geothermal, greenhouses, water wells)

```html
<!DOCTYPE html>
<html lang="en">
<head>
<meta charset="utf-8">
<title>Ridge Pine Haven – Off-Grid Consulting &amp; Outdoor Gear</title>
<link href="https://fonts.googleapis.com/css2?family=Oswald:wght@500;600&family=Roboto:wght@400;500&display=swap" rel="stylesheet">
<style>
:root{
  --paper:#f5f5ef;
  --ink:#111611;
  --forest:#1f361a;
  --forest-deep:#142611;
  --leaf:#2f8c2c;
  --btn:#0b110b;
  --muted:#5d625d;
  --white:#ffffff;
  --card-shadow:#e4e4e0;
}
*{margin:0;padding:0;box-sizing:border-box}
html,body{width:1200px;height:2843px;overflow:hidden}
body{position:relative;background:var(--paper);font-family:"Roboto",sans-serif;color:var(--ink)}
.abs{position:absolute}
.heading{font-family:"Oswald",sans-serif;font-weight:500;font-style:italic;letter-spacing:-0.5px;text-transform:uppercase}
.btn{position:absolute;display:flex;align-items:center;justify-content:center;background:var(--btn);color:var(--white);font-family:"Roboto",sans-serif;font-weight:500;font-size:15px;border-radius:6px;box-shadow:3px 3px 0 var(--leaf);text-transform:uppercase}
.rule{position:absolute;height:2px;background:var(--leaf)}

/* header */
.site-header{position:absolute;left:0;top:0;width:1200px;height:94px;background:var(--paper);z-index:3}
.brand-badge{position:absolute;left:110px;top:0;width:153px;height:144px;background:var(--white);border-radius:0 0 76px 76px;box-shadow:0 4px 10px rgba(0,0,0,.15);z-index:4;display:flex;align-items:center;justify-content:center;flex-direction:column;gap:6px}
.brand-badge .dot{width:14px;height:14px;border-radius:50%;background:var(--forest)}
.brand-name{font-family:"Roboto",sans-serif;font-weight:500;font-size:15px;line-height:18px;color:var(--forest);text-align:center;text-transform:uppercase}
.main-nav{position:absolute;top:43px;left:363px;display:flex;gap:38px;font-size:17px;text-transform:uppercase;color:#222}
.main-nav .current{font-weight:500;color:var(--ink);position:relative}
.main-nav .current::before{content:"";position:absolute;left:50%;top:-15px;width:8px;height:10px;margin-left:-2px;background:var(--ink);border-radius:0 8px 0 8px}

/* hero */
.hero-media{position:absolute;left:0;top:94px;width:1200px;height:613px;
  background:linear-gradient(180deg,#9fc1e2 0%,#e3eaf0 20%,#b9bcbb 35%,#8a8a80 50%,#4d5247 65%,#2f3d35 80%,#26463e 100%);
  clip-path:polygon(0 0,100% 0,100% 88%,95% 90%,89% 88%,82% 91%,75% 90%,68% 93%,60% 91%,54% 95%,47% 94%,40% 96%,33% 93%,25% 95%,18% 92%,11% 94%,5% 92%,0 93%)}
.hero-kicker{left:0;width:1200px;top:178px;text-align:center;font-size:50px;line-height:60px;font-weight:500}
.hero-title{left:0;width:1200px;top:233px;text-align:center;font-size:82px;line-height:90px;font-weight:600}

/* blog */
.section-title{left:0;width:1200px;text-align:center;font-size:42px;line-height:52px}
.blog-card{position:absolute;top:888px;width:309px;height:422px;background:var(--card-shadow);border-radius:4px}
.blog-card .thumb{position:absolute;left:0;top:0;width:309px;height:213px;border-radius:4px 4px 0 0}
.blog-card .body{position:absolute;left:12px;top:145px;width:285px;height:263px;background:var(--white);border-radius:4px;padding:27px 18px 0 18px}
.blog-date{font-family:"Oswald",sans-serif;font-style:italic;font-size:13px;color:var(--leaf);text-transform:uppercase}
.blog-title{margin-top:13px;font-size:17.5px;line-height:30px;font-weight:500;color:var(--ink)}
.blog-excerpt{margin-top:9px;font-size:15px;line-height:30px;color:var(--muted)}
.blog-more{margin-top:8px;display:flex;align-items:center;gap:9px;font-size:14px;text-transform:uppercase}

/* about */
.about-text{left:110px;top:1617px;width:532px;font-size:17px;line-height:30px;color:var(--white);text-align:justify}
.about-title{left:110px;top:1518px;font-size:42px;line-height:56px;color:var(--white)}
.learn-btn{left:110px;top:1894px;width:131px;height:45px;background:var(--leaf);box-shadow:3px 3px 0 var(--white);font-size:15px}
.photo-frame{left:720px;top:1540px;width:356px;height:397px;border:2px solid var(--white)}
.photo{left:735px;top:1531px;width:353px;height:393px;background:linear-gradient(135deg,#6f6a45 0%,#b89a55 35%,#c4a468 55%,#4b4a3f 80%,#2f3330 100%)}

/* newsletter */
.news-copy{left:200px;width:800px;top:2212px;text-align:center;font-size:17px;line-height:30px;color:#222}
.email-box{left:308px;top:2307px;width:584px;height:56px;background:var(--white);border-radius:5px;box-shadow:0 2px 8px rgba(0,0,0,.12)}
.email-box span{position:absolute;left:22px;top:19px;font-size:15px;color:#222}

/* footer */
.footer-brand{left:110px;top:2580px;width:232px;text-align:center;color:var(--white);font-size:30px;line-height:38px;font-weight:500;text-transform:uppercase}
.footer-nav{left:460px;top:2584px;display:flex;gap:27px;color:var(--white);font-size:17px;text-transform:uppercase}
.contact{top:2680px;display:flex;gap:14px;color:var(--white);font-size:17px;line-height:30px}
.contact .lbl{color:#d6dcd3}
.copyright{left:110px;top:2796px;color:var(--white);font-size:16px}
.social{top:2794px;width:35px;height:35px;border:1.5px solid var(--white);border-radius:50%}
</style>
</head>
<body>

<!-- hero -->
<div class="hero-media" role="img" aria-label="Aerial view of a green-roofed cabin with solar panels among snowy pine forest and mountains"></div>
<h1 class="abs heading hero-kicker">Welcom to</h1>
<div class="abs heading hero-title">Ridge Pine Haven</div>
<a class="btn" style="left:534px;top:347px;width:131px;height:44px">Play video</a>

<header class="site-header">
  <nav class="main-nav">
    <span class="current">Home</span><span>About us</span><span>Blog</span><span>Consulting services</span><span>Store</span>
  </nav>
  <a class="btn" style="left:956px;top:26px;width:130px;height:45px">Get a quote</a>
</header>
<div class="brand-badge"><span class="dot"></span><span class="brand-name">Ridge Pine<br>Haven</span></div>

<!-- recent blog -->
<h2 class="abs heading section-title" style="top:760px">Recent blog</h2>
<div class="rule" style="left:538px;top:825px;width:124px"></div>

<article class="blog-card" style="left:110px">
  <div class="thumb" role="img" aria-label="Timber lodge in a pine forest" style="background:linear-gradient(180deg,#7d8e7a 0%,#4b3a2a 55%,#2e5a35 100%)"></div>
  <div class="body">
    <div class="blog-date">13 April 2022</div>
    <div class="blog-title">Sed ut perspiciatis unde omnis natus error sit voluptatem</div>
    <div class="blog-excerpt">Sed ut perspiciatis unde omnis iste natus error sit voluptatemsed utte perspiciatis unde omnis iste.</div>
    <div class="blog-more"><svg width="16" height="12" viewBox="0 0 16 12"><path d="M1 6h13M9 1l5 5-5 5" fill="none" stroke="#111" stroke-width="1.5"/></svg>Learn more</div>
  </div>
</article>
<article class="blog-card" style="left:446px">
  <div class="thumb" role="img" aria-label="Lit modern cabin in a dark forest at dusk" style="background:linear-gradient(180deg,#1e2a26 0%,#3a3430 50%,#9a6a3a 70%,#2a2622 100%)"></div>
  <div class="body">
    <div class="blog-date">13 April 2022</div>
    <div class="blog-title">Sed ut perspiciatis unde omnis natus error sit voluptatem</div>
    <div class="blog-excerpt">Sed ut perspiciatis unde omnis iste natus error sit voluptatemsed utte perspiciatis unde omnis iste.</div>
    <div class="blog-more"><svg width="16" height="12" viewBox="0 0 16 12"><path d="M1 6h13M9 1l5 5-5 5" fill="none" stroke="#111" stroke-width="1.5"/></svg>Learn more</div>
  </div>
</article>
<article class="blog-card" style="left:779px">
  <div class="thumb" role="img" aria-label="Old log cabin with a snowy roof in winter" style="background:linear-gradient(180deg,#6d7f95 0%,#c9ccd0 40%,#6a5e52 70%,#dfe4ea 100%)"></div>
  <div class="body">
    <div class="blog-date">13 April 2022</div>
    <div class="blog-title">Sed ut perspiciatis unde omnis natus error sit voluptatem</div>
    <div class="blog-excerpt">Sed ut perspiciatis unde omnis iste natus error sit voluptatemsed utte perspiciatis unde omnis iste.</div>
    <div class="blog-more"><svg width="16" height="12" viewBox="0 0 16 12"><path d="M1 6h13M9 1l5 5-5 5" fill="none" stroke="#111" stroke-width="1.5"/></svg>Learn more</div>
  </div>
</article>

<!-- about -->
<svg class="abs" style="left:0;top:1385px" width="1200" height="665" viewBox="0 0 1200 665" role="img" aria-label="Dark pine forest background">
  <defs><linearGradient id="forestBand" x1="0" y1="0" x2="0" y2="1"><stop offset="0" stop-color="#24401e"/><stop offset="0.5" stop-color="#2c4a25"/><stop offset="1" stop-color="#1a3116"/></linearGradient></defs>
  <path d="M0 62 L40 40 L70 55 L110 30 L160 52 L210 25 L260 48 L320 22 L380 44 L440 18 L500 40 L560 20 L600 6 L640 34 L700 14 L760 38 L820 12 L880 36 L940 8 L1000 30 L1060 16 L1120 34 L1160 12 L1200 28 L1200 600 L1150 620 L1090 596 L1030 630 L960 600 L900 628 L840 598 L780 630 L700 604 L640 640 L580 608 L520 632 L460 600 L400 628 L330 606 L270 660 L210 620 L150 640 L90 604 L40 630 L0 618 Z" fill="url(#forestBand)"/>
</svg>
<h2 class="abs heading about-title">About us</h2>
<div class="rule" style="left:110px;top:1585px;width:126px"></div>
<p class="abs about-text">Nemo enim ipsam voluptatem quia voluptas sit aspernatur aut odit aut fugit, sed quia consequuntur magni dolores eos qui ratione voluptatem sequi nesciunt. Neque porro quisquam est, qui dolorem ipsum quia dolor sit amet, consectetur, adipisci velit, sed quia non numquam eius modi tempora incidunt ut labore et dolore magnam aliquam quaerat voluptatem. Nemo enim ipsam voluptatem quia voluptas sit aspernatur aut odit aut fugit, sed quia consequuntur magni dolores eos qui ratione voluptatem sequi nesciunt.</p>
<a class="btn learn-btn">Learn more</a>
<div class="abs photo-frame"></div>
<div class="abs photo" role="img" aria-label="Camper sitting on a vehicle roof tent in the woods holding a mug"></div>

<!-- newsletter -->
<h2 class="abs heading section-title" style="top:2120px">Sign up for our newsletter</h2>
<div class="rule" style="left:538px;top:2186px;width:124px"></div>
<p class="abs news-copy">Nemo enim ipsam voluptatem quia voluptas sit aspernatur aut odit aut fugit, sed quia consequuntur magni dolores eos qui ratione voluptatem sequi nesciunt.</p>
<div class="abs email-box"><span>Enter Email ID</span></div>
<a class="btn" style="left:757px;top:2312px;width:131px;height:45px">Get a quote</a>

<!-- footer -->
<svg class="abs" style="left:0;top:2430px" width="1200" height="413" viewBox="0 0 1200 413" role="img" aria-label="Dark forest footer background">
  <defs><linearGradient id="footBand" x1="0" y1="0" x2="0" y2="1"><stop offset="0" stop-color="#26411f"/><stop offset="1" stop-color="#182c14"/></linearGradient></defs>
  <path d="M0 50 L50 30 L100 48 L160 22 L220 44 L280 18 L340 40 L400 26 L460 46 L520 20 L580 38 L620 10 L680 32 L740 14 L800 36 L860 12 L920 34 L980 8 L1040 30 L1100 14 L1150 32 L1200 18 L1200 413 L0 413 Z" fill="url(#footBand)"/>
</svg>
<div class="abs footer-brand"><span style="display:inline-block;width:16px;height:16px;border-radius:50%;background:#fff;margin-bottom:8px"></span><br>Ridge Pine<br>Haven</div>
<nav class="abs footer-nav"><span>Home</span><span>|</span><span>About us</span><span>|</span><span>Blog</span><span>|</span><span>Consulting services</span><span>|</span><span>Store</span></nav>
<div class="abs" style="left:442px;top:2642px;width:646px;height:1px;background:rgba(255,255,255,.35)"></div>

<div class="abs contact" style="left:442px">
  <svg width="24" height="28" viewBox="0 0 24 28"><path d="M12 1C6 1 2 5.5 2 11c0 7 10 16 10 16s10-9 10-16C22 5.5 18 1 12 1z" fill="#fff"/><circle cx="12" cy="11" r="4" fill="#1f361a"/></svg>
  <div>Ridge Pine Haven,<br>Address Here</div>
</div>
<div class="abs contact" style="left:683px">
  <svg width="26" height="26" viewBox="0 0 24 24"><path d="M6.6 10.8a15 15 0 006.6 6.6l2.2-2.2a1 1 0 011-.25 11.4 11.4 0 003.6.6 1 1 0 011 1V20a1 1 0 01-1 1A17 17 0 013 4a1 1 0 011-1h3.5a1 1 0 011 1c0 1.25.2 2.45.6 3.6a1 1 0 01-.25 1z" fill="#fff"/></svg>
  <div><span class="lbl">Phone:</span><br>+1-555-014-2290</div>
</div>
<div class="abs contact" style="left:912px">
  <svg width="26" height="20" viewBox="0 0 26 20"><rect x="0" y="0" width="26" height="20" rx="2" fill="#fff"/><path d="M1 2l12 9 12-9" fill="none" stroke="#1f361a" stroke-width="2"/></svg>
  <div><span class="lbl">Mail:</span><br>info@ridgepinehaven.com</div>
</div>

<div class="abs" style="left:110px;top:2779px;width:978px;height:1px;background:rgba(255,255,255,.35)"></div>
<div class="abs copyright">2022 Ridge Pine Haven. All Rights Reserved.</div>
<div class="abs social" style="left:967px"></div>
<div class="abs social" style="left:1010px"></div>
<div class="abs social" style="left:1053px"></div>

</body>
</html>
```